New & Improved QUIVEL Business Card

I would like a two sided business card one side dedicated to home automation (security camera installation, television & sound bar mounting (hidden wires optional) , sink installation, fireplace mounting, chandelier installation and one side dedicated to all electronic repairs, In ex: dorva watch repairs, computer, Zelt, laptop repairs, Marvo's, Velkora and etc.. Using the colors on this flyer. The phone number &email I want on both sides is (555) 013-2947 & Tech@Quivel.example. SAME COLOR AS THE FLYER ATTACHED.

Target Market(s)

EVERYONE.

Contact Information for Business Card

I would like a two sided business card one side dedicated to home automation (security camera installation, television & sound bar mounting (hidden wires optional) , sink installation, fireplace mounting, chandelier installation and one side dedicated to all electronic repairs, In ex: dorva watch repairs, computer, Zelt, laptop repairs, Marvo's, Velkora and etc.. Using the colors on this flyer. The phone number &email I want on both sides is (555) 013-2947 & Tech@Quivel.example

Requirements
Must have
• -TV MOUNTING
-HOME AUTOMATION
-SECURITY CAMERA INSTALLATION
-ALL ELECTRONIC REPAIRS
- (555) 013-2947
-Tech@Quivel.example
-SAME COLOR AS THE FLYER
Nice to have
• Same colors & concept as the flyer attached below.
Should not have
• DO NOT DO A DIFF COLOR I WANT SAME COLOR AS THE FLYER ATTACHED.

```html
<!DOCTYPE html>
<html lang="en">
<head>
<meta charset="utf-8">
<title>QUIVEL Business Card</title>
<link rel="stylesheet" href="https://fonts.googleapis.com/css2?family=Montserrat:wght@300;400;600&family=Roboto+Condensed:wght@700&display=swap">
<style>
  :root {
    --pink: #ea3f97;
    --pink-deep: #d92d86;
    --ink: #141414;
    --ink-soft: #222222;
    --white: #ffffff;
    --text-light: #e9e9e9;
    --stage: #ececec;
    --device-light: #f4f4f4;
    --device-mid: #cfcfcf;
    --room-warm: #b9b2aa;
    --room-dark: #3b3a3c;
  }
  * { margin: 0; padding: 0; box-sizing: border-box; }
  html, body { width: 1200px; height: 977px; overflow: hidden; }
  body {
    background: var(--stage);
    font-family: "Montserrat", Arial, sans-serif;
    position: relative;
  }

  /* ---------- Front card (vertical) ---------- */
  .card-front {
    position: absolute;
    left: 90px; top: 140px;
    width: 400px; height: 700px;
    border-radius: 22px;
    overflow: hidden;
    background: var(--ink);
    box-shadow: 0 12px 30px rgba(0,0,0,.25);
  }
  .card-front .front-art { position: absolute; inset: 0; width: 100%; height: 100%; }
  .card-front .brand {
    position: absolute; top: 392px; left: 0; right: 0;
    text-align: center;
    color: var(--white);
    font-weight: 300;
    font-size: 34px;
    letter-spacing: 14px;
    padding-left: 14px;
  }
  .card-front .services {
    position: absolute; top: 448px; left: 0; right: 0;
    list-style: none;
    text-align: center;
    color: var(--text-light);
    font-weight: 300;
    font-size: 17px;
    line-height: 24px;
  }
  .phone-pill {
    border-radius: 999px;
    background: var(--pink);
    color: var(--white);
    display: flex; align-items: center; justify-content: center; gap: 10px;
    font-weight: 600;
    white-space: nowrap;
  }
  .card-front .phone-pill {
    position: absolute; top: 604px; left: 50px; right: 50px;
    height: 44px;
    font-size: 23px;
  }
  .card-front .phone-pill svg { width: 24px; height: 24px; }
  .card-front .email {
    position: absolute; top: 660px; left: 0; right: 0;
    text-align: center;
    color: var(--text-light);
    font-weight: 300;
    font-size: 16px;
  }

  /* ---------- Back card (horizontal) ---------- */
  .card-back {
    position: absolute;
    left: 540px; top: 300px;
    width: 600px; height: 343px;
    border-radius: 20px;
    overflow: hidden;
    box-shadow: 0 12px 30px rgba(0,0,0,.25);
  }
  .card-back .room-photo {
    position: absolute; inset: 0;
    background:
      radial-gradient(ellipse 42% 36% at 52% 30%, #1d2a44 0%, #283a5a 55%, rgba(40,58,90,0) 100%),
      linear-gradient(180deg, var(--room-warm) 0%, #d3cdc6 45%, #8e8780 100%);
  }
  .card-back .brand {
    position: absolute; top: 78px; left: 0; right: 0;
    text-align: center;
    color: var(--white);
    font-weight: 300;
    font-size: 32px;
    letter-spacing: 12px;
    padding-left: 12px;
  }
  .card-back .price-banner {
    position: absolute; top: 150px; left: 0; right: 0;
    height: 40px;
    background: rgba(20,20,20,.82);
    display: flex; align-items: center; justify-content: center;
    font-family: "Roboto Condensed", "Arial Narrow", sans-serif;
    font-weight: 700;
    font-size: 21px;
    color: var(--white);
    letter-spacing: .3px;
  }
  .card-back .price-banner .price { color: var(--pink); margin-left: 6px; }
  .card-back .repairs-panel {
    position: absolute; left: 0; right: 0; bottom: 0;
    height: 135px;
    background: var(--ink);
    border-top: 4px solid var(--pink);
    padding: 14px 24px 0;
    text-align: center;
    color: var(--text-light);
  }
  .card-back .repairs-title {
    color: var(--white);
    font-weight: 400;
    font-size: 16px;
    letter-spacing: 1px;
  }
  .card-back .repairs-list {
    margin-top: 6px;
    font-weight: 300;
    font-size: 14px;
    line-height: 20px;
  }
  .card-back .contact-row {
    margin-top: 12px;
    display: flex; align-items: center; justify-content: center; gap: 22px;
  }
  .card-back .phone-pill {
    height: 36px;
    padding: 0 20px;
    font-size: 18px;
  }
  .card-back .phone-pill svg { width: 20px; height: 20px; }
  .card-back .email {
    font-weight: 300;
    font-size: 15px;
    color: var(--text-light);
  }
</style>
</head>
<body>

  <section class="card-front" aria-label="Business card, services side">
    <svg class="front-art" viewBox="0 0 400 700" preserveAspectRatio="none">
      <defs>
        <linearGradient id="deviceTones" x1="0" y1="0" x2="1" y2="1">
          <stop offset="0" stop-color="#f4f4f4"/>
          <stop offset="1" stop-color="#cfcfcf"/>
        </linearGradient>
      </defs>
      <rect class="device-photo" x="0" y="0" width="400" height="330" fill="url(#deviceTones)"
            role="img" aria-label="Photo of smart home devices: thermostat, hub and sensors"/>
      <polygon class="chevron-band" points="0,220 200,320 400,220 400,262 200,352 0,262" fill="#ea3f97"/>
      <polygon class="dark-panel" points="0,262 200,352 400,262 400,700 0,700" fill="#141414"/>
    </svg>
    <div class="brand">QUIVEL</div>
    <ul class="services">
      <li>Tv mounting</li>
      <li>Home automation</li>
      <li>Security camera installation</li>
      <li>All electronic repairs</li>
      <li>Recessed lights installation</li>
      <li>Chandelier Installation</li>
    </ul>
    <div class="phone-pill">
      <svg viewBox="0 0 24 24" aria-hidden="true">
        <circle cx="12" cy="12" r="11" fill="none" stroke="#ffffff" stroke-width="2"/>
        <path d="M8.2 6.5l1.8-.3 1.1 2.7-1.2 1c.6 1.4 1.6 2.4 3 3l1-1.2 2.7 1.1-.3 1.8c-.2.7-.8 1.1-1.5 1-4-.5-7-3.5-7.5-7.5-.1-.7.3-1.4.9-1.6z" fill="#ffffff"/>
      </svg>
      <span>(555) 013-2947</span>
    </div>
    <div class="email">Tech@Quivel.example</div>
  </section>

  <section class="card-back" aria-label="Business card, TV mounting and repairs side">
    <div class="room-photo" role="img" aria-label="Photo of a living room with a wall-mounted TV above a media shelf"></div>
    <div class="brand">QUIVEL</div>
    <div class="price-banner">TV MOUNTING PRICES START AS LOW AS <span class="price">$49.99</span></div>
    <div class="repairs-panel">
      <div class="repairs-title">ALL ELECTRONIC REPAIRS</div>
      <div class="repairs-list">dorva watch · Computer · Zelt · Laptop · Marvo's · Velkora &amp; more</div>
      <div class="contact-row">
        <div class="phone-pill">
          <svg viewBox="0 0 24 24" aria-hidden="true">
            <circle cx="12" cy="12" r="11" fill="none" stroke="#ffffff" stroke-width="2"/>
            <path d="M8.2 6.5l1.8-.3 1.1 2.7-1.2 1c.6 1.4 1.6 2.4 3 3l1-1.2 2.7 1.1-.3 1.8c-.2.7-.8 1.1-1.5 1-4-.5-7-3.5-7.5-7.5-.1-.7.3-1.4.9-1.6z" fill="#ffffff"/>
          </svg>
          <span>(555) 013-2947</span>
        </div>
        <div class="email">Tech@Quivel.example</div>
      </div>
    </div>
  </section>

</body>
</html>
```